Marlowe Sail Works President Business Card Carbon fiber catamarans

Hi.. I need a new business card design.. I am the President of a high tech yacht builder. We build Carbon Fiber go fast catamarans... Maybe we use the file I am sharing to you as the back of the card.. We need to look cool and crisp ...

Target Market(s)

Affluent People who will purchase a cool yacht

Industry/Entity Type

Custom Yacht Builder

Contact Information for Business Card

Dean Pellington , President, 512.608.3419 USA

Font styles to use
Serif

Requirements
Must have
• the clean crisp cool feel
Nice to have
• clean and crisp
Should not have
• Bold ugly

```html
<!DOCTYPE html>
<html lang="en">
<head>
<meta charset="utf-8">
<title>Marlowe Sail Works — Business Card</title>
<link rel="stylesheet" href="https://fonts.googleapis.com/css2?family=Montserrat:wght@400;600&display=swap">
<style>
  :root {
    --backdrop: #2a2a2c;
    --card-dark: #0d0d0e;
    --card-mid: #1c1c1e;
    --silver: #d6d8da;
    --text-light: #e4e4e4;
    --text-soft: #b4b4b6;
    --faint-mark: rgba(255,255,255,0.05);
  }
  * { margin: 0; padding: 0; box-sizing: border-box; }
  html, body {
    width: 1200px; height: 874px; overflow: hidden;
    background: var(--backdrop);
    font-family: "Montserrat", sans-serif;
  }
  .canvas {
    position: relative; width: 1200px; height: 874px;
  }
  .card {
    position: absolute; left: 320px; width: 560px; height: 320px;
    overflow: hidden;
    box-shadow: 0 14px 30px rgba(0,0,0,0.45);
  }
  .card-front { top: 107px; }
  .card-back { top: 447px; }
  .card-surface {
    position: absolute; inset: 0;
    background: radial-gradient(ellipse at 40% 35%, var(--card-mid), var(--card-dark) 75%);
  }
  .brand {
    position: absolute; display: flex; align-items: center; gap: 14px;
    color: var(--silver); font-weight: 600; letter-spacing: 0.22em;
    text-transform: uppercase; white-space: nowrap;
  }
  .brand-dot {
    width: 34px; height: 34px; border-radius: 50%;
    background: var(--silver); flex: none;
  }
  .card-front .brand {
    left: 0; right: 0; top: 142px; justify-content: center; font-size: 28px;
  }
  .card-back .brand { left: 40px; top: 46px; font-size: 20px; }
  .faint-mark {
    position: absolute; right: 40px; top: 90px;
    width: 230px; height: 230px; border-radius: 50%;
    background: var(--faint-mark);
  }
  .contact { position: absolute; left: 40px; top: 110px; color: var(--text-light); }
  .person-name { font-size: 17px; font-weight: 600; letter-spacing: 0.03em; text-transform: uppercase; }
  .person-title { font-size: 12px; color: var(--text-soft); margin-top: 2px; }
  .address { font-size: 12px; color: var(--text-soft); margin-top: 18px; line-height: 1.45; }
  .contact-list { list-style: none; margin-top: 14px; font-size: 12px; color: var(--text-soft); line-height: 1.7; }
  .contact-list li { display: flex; align-items: center; gap: 8px; }
  .contact-list svg { width: 10px; height: 10px; fill: var(--text-light); flex: none; }
</style>
</head>
<body>
<main class="canvas">
  <section class="card card-front">
    <div class="card-surface" role="img" aria-label="Dark perforated carbon texture"></div>
    <div class="brand"><span class="brand-dot"></span>Marlowe Sail Works</div>
  </section>

  <section class="card card-back">
    <div class="card-surface" role="img" aria-label="Dark perforated carbon texture"></div>
    <div class="faint-mark"></div>
    <div class="brand">Marlowe Sail Works</div>
    <div class="contact">
      <p class="person-name">Dean Pellington</p>
      <p class="person-title">President</p>
      <p class="address">2140 Harbor Point Drive<br>Austin, Texas 78701</p>
      <ul class="contact-list">
        <li><svg viewBox="0 0 10 10"><path d="M2 0.5 L3.6 2.6 L2.8 3.6 Q4 6 6.4 7.2 L7.4 6.4 L9.5 8 L8.4 9.6 Q3 9 0.4 1.6 Z"/></svg>512.608.3419</li>
        <li><svg viewBox="0 0 10 10"><path d="M0 2 H10 V8.5 H0 Z M0.6 2.4 L5 5.6 L9.4 2.4" stroke="#0d0d0e" stroke-width="0.8"/></svg>info@marlowesail.com</li>
        <li><svg viewBox="0 0 10 10"><circle cx="5" cy="5" r="4.6"/><path d="M0.6 5 H9.4 M5 0.4 V9.6" stroke="#0d0d0e" stroke-width="0.8"/></svg>www.marlowesail.com</li>
      </ul>
    </div>
  </section>
</main>
</body>
</html>
```